Design of two graphics from basic existing design & colours

I have two graphics which I currently use but they are nothing special. We would like to transform these two graphics, using our existing logo colour, into something special. The outputs will be used:

- on our website;
- in a powerpoint sales presentation;
- in email campaigns; and
- to print for handing to prospects at the end of a sales presentation.

Please just submit one of the graphics and if we like the design, we will ask you to work on the second graphic. These two graphics are critical to our marketing and will be used together so we need them to have a similar look and feel.

```html
<!DOCTYPE html>
<html lang="en">
<head>
<meta charset="utf-8">
<title>Leadership Framework</title>
<link href="https://fonts.googleapis.com/css2?family=Source+Sans+3:wght@400;600&family=Ubuntu:wght@700&display=swap" rel="stylesheet">
<style>
  :root {
    --canvas: #dcdcdc;
    --card: #ffffff;
    --ink: #1a1a1a;
    --cultural: #6e1400;
    --strategic: #e31b23;
    --operational: #a60202;
    --financial: #e35c47;
    --brand: #8a1408;
    --card-shadow: rgba(40, 60, 90, 0.35);
  }
  * { box-sizing: border-box; margin: 0; padding: 0; }
  html, body { width: 1200px; height: 1105px; overflow: hidden; background: var(--canvas); }
  .framework { position: relative; width: 1200px; height: 1105px; font-family: "Source Sans 3", sans-serif; color: var(--ink); }

  .tab {
    position: absolute; width: 404px; height: 60px;
    display: flex; align-items: center; justify-content: center;
    font-family: "Ubuntu", sans-serif; font-weight: 700; font-size: 29px; color: #fff;
  }
  .tab--top { top: 122px; border-radius: 24px 24px 0 0; padding-bottom: 6px; }
  .tab--top::after {
    content: ""; position: absolute; left: 0; right: 0; bottom: 0; height: 14px;
    background: radial-gradient(ellipse at 50% 100%, rgba(0,0,0,0.45), rgba(0,0,0,0) 70%);
  }
  .tab--bottom { top: 934px; border-radius: 0 0 24px 24px; padding-top: 4px; }
  .tab--bottom::before {
    content: ""; position: absolute; left: 0; right: 0; top: 0; height: 14px;
    background: radial-gradient(ellipse at 50% 0%, rgba(0,0,0,0.45), rgba(0,0,0,0) 70%);
  }
  .tab--cultural { left: 145px; background: var(--cultural); }
  .tab--strategic { left: 623px; background: var(--strategic); }
  .tab--operational { left: 145px; background: var(--operational); }
  .tab--financial { left: 623px; background: var(--financial); }

  .card { position: absolute; background: var(--card); width: 455px; }
  .card--top { top: 182px; height: 371px; }
  .card--bottom { top: 573px; height: 361px; }
  .card--left { left: 119px; }
  .card--right { left: 598px; }
  .card--top::after {
    content: ""; position: absolute; left: 4px; right: 4px; bottom: -12px; height: 12px;
    background: radial-gradient(ellipse at 50% 0%, var(--card-shadow), rgba(0,0,0,0) 70%);
  }

  .topics { position: absolute; list-style: none; font-size: 29px; line-height: 37px; }
  .topics li::before { content: "•"; font-size: 20px; margin-right: 6px; position: relative; top: -3px; }

  .hub {
    position: absolute; left: 439px; top: 411px; width: 290px; height: 290px;
    border-radius: 50%; background: var(--canvas);
  }
  .hub__face {
    position: absolute; left: 23px; top: 23px; width: 244px; height: 244px; border-radius: 50%;
    background: var(--card); box-shadow: 5px 7px 10px rgba(0,0,0,0.45);
    display: flex; flex-direction: column; align-items: center; justify-content: center;
  }
  .brand-name {
    font-family: "Source Sans 3", sans-serif; font-weight: 600; color: var(--brand);
    font-size: 27px; line-height: 28px; text-align: center; letter-spacing: 1px; margin-top: 18px;
  }
  .brand-dot { width: 40px; height: 40px; border-radius: 50%; background: var(--brand); }
</style>
</head>
<body>
<main class="framework">
  <div class="card card--top card--left">
    <ul class="topics" style="left:27px; top:63px;">
      <li>Coaching</li><li>Communication</li><li>Competencies</li><li>Development</li><li>Employment</li>
    </ul>
    <ul class="topics" style="left:257px; top:63px;">
      <li>Leadership</li><li>Performance</li><li>Profiles</li><li>Succession</li><li>Team</li>
    </ul>
  </div>
  <div class="card card--top card--right">
    <ul class="topics" style="left:120px; top:57px;">
      <li>Board</li><li>Purpose</li><li>Risk</li><li>Stragedy</li><li>Structure</li><li>Values</li><li>Vision</li>
    </ul>
  </div>
  <div class="card card--bottom card--left">
    <ul class="topics" style="left:28px; top:96px;">
      <li>Competitor</li><li>Compliance</li><li>Customer</li><li>Marketing</li><li>Meeting</li>
    </ul>
    <ul class="topics" style="left:236px; top:96px;">
      <li>Planning</li><li>Policy</li><li>Projects</li><li>Reporting</li><li>Review</li>
    </ul>
  </div>
  <div class="card card--bottom card--right">
    <ul class="topics" style="left:122px; top:96px;">
      <li>Budget</li><li>CAPEX</li><li>Cash Flow</li><li>Delegations</li><li>OPEX</li>
    </ul>
  </div>

  <div class="tab tab--top tab--cultural">Cultural</div>
  <div class="tab tab--top tab--strategic">Strategic</div>
  <div class="tab tab--bottom tab--operational">Operational</div>
  <div class="tab tab--bottom tab--financial">Financial</div>

  <div class="hub">
    <div class="hub__face">
      <div class="brand-dot"></div>
      <div class="brand-name">CORVANA<br>LEADERSHIP</div>
    </div>
  </div>
</main>
</body>
</html>
```